New Business Card Design Project

I would like my card design to look exactly like the logo, design, layout, and print of the current attached file. The only change I would like made would be for the print to say THE KMR GROUP instead of THE MORALES GROUP. Basically, just replace his group name with my group name. I would also like the backgroud to be the same texture and color as the attached file. I love the dark blue lettering and house logo on the card.

I am completely open to the rest of the card design. I just want something clean and simple. Only basic contact info required on the card. Maybe just name: Wade K Holmer and cell # 555.014.2289 and email wade@kmrgroup.example

```html
<!DOCTYPE html>
<html lang="en">
<head>
<meta charset="utf-8">
<title>The KMR Group – Business Card</title>
<link rel="stylesheet" href="https://fonts.googleapis.com/css2?family=Montserrat:wght@400&family=Arimo:wght@400;700&display=swap">
<style>
  :root {
    --backdrop: #3b3431;
    --card-white: #f4f4f2;
    --navy: #12132f;
    --ink: #15163a;
    --grey-text: #555659;
    --silver: #c9cacd;
    --divider: #cfd0d2;
  }
  * { box-sizing: border-box; margin: 0; padding: 0; }
  html, body {
    width: 1200px; height: 844px; overflow: hidden;
    background: var(--backdrop);
  }
  .canvas {
    position: relative; width: 1200px; height: 844px;
    display: flex; align-items: center; justify-content: center; gap: 60px;
  }
  .card {
    position: relative; width: 525px; height: 300px;
    box-shadow: 0 10px 28px rgba(0,0,0,.45);
  }
  .card--front { background: var(--card-white); }
  .card--back  { background: var(--navy); display: flex; align-items: center; justify-content: center; }

  .brand { display: flex; align-items: center; gap: 18px; }
  .brand__square { width: 64px; height: 64px; flex: none; }
  .brand__name {
    font-family: "Montserrat", sans-serif; font-weight: 400;
    font-size: 22px; line-height: 1.12; letter-spacing: .2em; text-transform: uppercase;
  }
  .card--front .brand { position: absolute; left: 40px; top: 118px; }
  .card--front .brand__square { background: var(--ink); }
  .card--front .brand__name { color: var(--ink); }

  .card--back .brand { gap: 22px; }
  .card--back .brand__square { width: 80px; height: 80px; background: var(--silver); }
  .card--back .brand__name { color: var(--silver); font-size: 27px; }

  .front__divider {
    position: absolute; left: 300px; top: 70px; width: 1px; height: 150px;
    background: var(--divider);
  }
  .contact { position: absolute; left: 330px; top: 104px; }
  .contact__name {
    font-family: "Arimo", sans-serif; font-weight: 700; font-size: 17px;
    color: var(--ink); letter-spacing: .02em; text-transform: uppercase; margin-bottom: 22px;
  }
  .contact__line {
    display: flex; align-items: center; gap: 7px;
    font-family: "Arimo", sans-serif; font-size: 14px; color: var(--grey-text); margin-bottom: 5px;
    white-space: nowrap;
  }
  .contact__icon { width: 11px; height: 11px; flex: none; }
</style>
</head>
<body>
<main class="canvas">
  <section class="card card--front" aria-label="Card front">
    <div class="brand">
      <span class="brand__square"></span>
      <p class="brand__name">The<br>KMR<br>Group</p>
    </div>
    <span class="front__divider"></span>
    <div class="contact">
      <p class="contact__name">Wade K Holmer</p>
      <p class="contact__line">
        <svg class="contact__icon" viewBox="0 0 11 11"><rect x="2.5" y="0.5" width="6" height="10" rx="1" fill="none" stroke="#15163a" stroke-width="1.2"/><rect x="4.5" y="8.3" width="2" height="1" fill="#15163a"/></svg>
        555.014.2289
      </p>
      <p class="contact__line">
        <svg class="contact__icon" viewBox="0 0 11 11"><rect x="0.5" y="2" width="10" height="7" fill="#15163a"/><path d="M0.8 2.3 L5.5 6 L10.2 2.3" fill="none" stroke="#f4f4f2" stroke-width="1"/></svg>
        wade@kmrgroup.example
      </p>
    </div>
  </section>

  <section class="card card--back" aria-label="Card back">
    <div class="brand">
      <span class="brand__square"></span>
      <p class="brand__name">The<br>KMR<br>Group</p>
    </div>
  </section>
</main>
</body>
</html>
```